Blue Harbor Business Cards

Name Tomas Welbridge
Title Mortgage Originator
Phone (800) 614-2290 x32
Direct (571) 362-0471
Email twelbridge@blueharborhomeloans.com
NMLS #1847362
Name Lena Ortiz
Title Mortgage Originator
Location (800) 614-2290 x55
Direct (440) 276-5190
Email lortiz@blueharborhomeloans.com
NMLS #2739418
Name Desmond Holloway-Finch
Title Mortgage Originator
Location (800) 614-2290 x56
Direct (202) 634-1975
Email dhollowayfinch@blueharborhomeloans.com
NMLS #2784530
Name Rosalyn Whitaker
Title Mortgage Originator
Location (800) 614-2290 x57
Direct (240) 358-6621
Email rwhitaker@blueharborhomeloans.com
NMLS #2491086
Name Gwen Holbrook
Title Mortgage Originator
Location (800) 614-2290 x58
Direct (540) 716-2384
Email gholbrook@blueharborhomeloans.com
NMLS #2438617
Name Ravi Dunmore
Title Mortgage Originator
Location (800) 614-2290 x59
Direct (240) 563-8827
Email rdunmore@blueharborhomeloans.com
NMLS #2597142
Name Ivy Marlow
Title Mortgage Originator
Location (800) 614-2290 x60
Direct (202) 479-3306
Email ivy@ivyfindshomes.com
NMLS #2718394
Contact Information for Business Card
Name Tomas Welbridge Title Mortgage Originator Phone (800) 614-2290 x32 Direct (571) 362-0471 Email twelbridge@blueharborhomeloans.com NMLS #1847362 Name Lena Ortiz Title Mortgage Originator Location (800) 614-2290 x55 Direct (440) 276-5190 Email lortiz@blueharborhomeloans.com NMLS #2739418 Name Desmond Holloway-Finch Title Mortgage Originator Location (800) 614-2290 x56 Direct (202) 634-1975 Email dhollowayfinch@blueharborhomeloans.com NMLS #2784530 Name Rosalyn Whitaker Title Mortgage Originator Location (800) 614-2290 x57 Direct (240) 358-6621 Email rwhitaker@blueharborhomeloans.com NMLS #2491086 Name Gwen Holbrook Title Mortgage Originator Location (800) 614-2290 x58 Direct (540) 716-2384 Email gholbrook@blueharborhomeloans.com NMLS #2438617 Name Ravi Dunmore Title Mortgage Originator Location (800) 614-2290 x59 Direct (240) 563-8827 Email rdunmore@blueharborhomeloans.com NMLS #2597142 Name Ivy Marlow Title Mortgage Originator Location (800) 614-2290 x60 Direct (202) 479-3306 Email ivy@ivyfindshomes.com NMLS #2718394
Look and feel
Each slider illustrates characteristics of the customer's brand and the style your logo design should communicate.

```html
<!DOCTYPE html>
<html lang="en">
<head>
<meta charset="utf-8">
<title>Blue Harbor Business Card – Tomas Welbridge</title>
<link rel="stylesheet" href="https://fonts.googleapis.com/css2?family=Archivo:wght@400;500;600;700&family=Montserrat:wght@700;800&display=swap">
<style>
  :root {
    --brand-green: #7cb46b;
    --photo-green: #9fcf8a;
    --ink: #3d3d3d;
    --ink-soft: #4a4a4a;
    --paper: #ffffff;
    --backdrop: #f1f2f2;
  }
  * { box-sizing: border-box; margin: 0; padding: 0; }
  html, body {
    width: 1200px; height: 1200px; overflow: hidden;
    background: var(--backdrop);
    font-family: "Archivo", Arial, sans-serif;
  }
  .card {
    position: absolute;
    left: 212px;
    width: 776px;
    height: 443px;
    box-shadow: 0 14px 22px rgba(0,0,0,0.16);
  }
  .card--front { top: 86px; background: var(--paper); }
  .card--back { top: 671px; background: var(--brand-green); }

  .front__band {
    position: absolute; left: 0; top: 0;
    width: 100%; height: 170px;
    background: var(--brand-green);
  }
  .front__name {
    position: absolute; left: 65px; top: 98px;
    font-size: 50px; line-height: 1; letter-spacing: -1.5px;
    color: var(--paper); font-weight: 400; white-space: nowrap;
  }
  .front__name strong { font-weight: 700; }
  .front__portrait {
    position: absolute; left: 525px; top: 82px;
    width: 170px; height: 170px;
  }
  .front__title {
    position: absolute; left: 65px; top: 184px;
    font-size: 17px; font-weight: 600; letter-spacing: 1.3px;
    color: var(--ink); word-spacing: 3px;
  }
  .front__nmls {
    position: absolute; left: 65px; top: 214px;
    font-size: 16.5px; font-weight: 600; color: var(--ink);
  }
  .front__nmls span { color: var(--brand-green); margin-right: 3px; }

  .contact-list {
    position: absolute; left: 65px; top: 298px;
    list-style: none;
  }
  .contact-list li {
    display: flex; align-items: center;
    height: 38px;
    font-size: 16.5px; color: var(--ink-soft); letter-spacing: 0.2px;
  }
  .contact-list svg { width: 26px; height: 26px; margin-right: 18px; flex: none; }

  .back__rule {
    position: absolute; left: 138px; top: 117px;
    width: 3px; height: 210px; background: var(--paper);
  }
  .back__logo {
    position: absolute; left: 163px; top: 210px;
    color: var(--paper); font-family: "Montserrat", Arial, sans-serif;
  }
  .back__logo-name { font-size: 27px; font-weight: 800; letter-spacing: 1.8px; line-height: 1; }
  .back__logo-slogan { font-size: 16px; font-weight: 800; letter-spacing: 8.5px; line-height: 1; margin-top: 3px; }
</style>
</head>
<body>

<section class="card card--front" aria-label="Business card front">
  <div class="front__band"></div>
  <h1 class="front__name"><strong>Tomas</strong> Welbridge</h1>

  <svg class="front__portrait" viewBox="0 0 170 170" aria-hidden="false">
    <circle cx="85" cy="85" r="83" fill="var(--paper)"/>
    <circle cx="85" cy="85" r="80" fill="var(--brand-green)"/>
    <circle cx="85" cy="85" r="74" fill="var(--paper)"/>
    <g role="img" aria-label="Portrait photo of Tomas Welbridge">
      <circle cx="85" cy="85" r="70" fill="url(#portraitTone)"/>
    </g>
    <defs>
      <linearGradient id="portraitTone" x1="0" y1="0" x2="0" y2="1">
        <stop offset="0" stop-color="#f4f4f2"/>
        <stop offset="0.55" stop-color="#e3e6e0"/>
        <stop offset="0.75" stop-color="var(--photo-green)"/>
        <stop offset="1" stop-color="#8cc07a"/>
      </linearGradient>
    </defs>
  </svg>

  <p class="front__title">MORTGAGE ORIGINATOR</p>
  <p class="front__nmls"><span>NMLS</span>#1847362</p>

  <ul class="contact-list">
    <li>
      <svg viewBox="0 0 26 26" aria-hidden="true" fill="none" stroke="var(--brand-green)" stroke-width="1.2">
        <circle cx="13" cy="13" r="12"/>
        <path d="M8.5 8c.8-.9 1.6-.9 2.1 0l1 1.7c.3.6.1 1.1-.4 1.5l-.6.5c.6 1.5 1.7 2.7 3.2 3.3l.5-.6c.4-.5 1-.6 1.5-.3l1.7 1c.8.5.8 1.3 0 2.1-1 1-2.4 1.1-4.1.2-2.1-1.1-3.9-3-5-5.1-.8-1.8-.8-3.2.1-4.3z"/>
      </svg>
      (800) 614-2290 x32
    </li>
    <li>
      <svg viewBox="0 0 26 26" aria-hidden="true" fill="none" stroke="var(--brand-green)" stroke-width="1.2">
        <circle cx="13" cy="13" r="12"/>
        <rect x="9.5" y="7" width="7" height="12" rx="1.2"/>
        <line x1="12" y1="17" x2="14" y2="17"/>
      </svg>
      (571) 362-0471
    </li>
    <li>
      <svg viewBox="0 0 26 26" aria-hidden="true" fill="none" stroke="var(--brand-green)" stroke-width="1.2">
        <circle cx="13" cy="13" r="12"/>
        <rect x="7.5" y="9" width="11" height="8" rx="0.8"/>
        <path d="M7.8 9.4L13 13.5l5.2-4.1"/>
      </svg>
      twelbridge@blueharborhomeloans.com
    </li>
  </ul>
</section>

<section class="card card--back" aria-label="Business card back">
  <div class="back__rule"></div>
  <div class="back__logo">
    <p class="back__logo-name">BUSINESS LOGO</p>
    <p class="back__logo-slogan">SLOGAN</p>
  </div>
</section>

</body>
</html>
```